Corporate Design für Metall-Bauteile-Fertigung
Zielgruppe
www.krl-fertek.de siehe als Infogrundlage
Metall-Bauteile Fertigung als Dienstleister
Zielgruppe Kunden und Lieferanten in der Metall- Industie
Vielfältige Fertigungsmöglichkeiten Dreh/Fräs CNC Bearbeitung,Baugruppen,Draht-und Senkerodieren,Schweißbaugruppen
Aufgabenstellung
Achtung Briefpapier Design bitte nach DIN 5008 für Geschäftspapiere mit Falts Markierung.
Visitenkarten mit Logo und in Anpassungsfähige Formate erstellen.
Blickfang ,Vertrauen, Tradition,Flexibel,Schnelligkeit. Präzision,Qualität

```html
<!DOCTYPE html>
<html lang="de">
<head>
<meta charset="utf-8">
<title>KRL Fertek GmbH – Geschäftsausstattung</title>
<link href="https://fonts.googleapis.com/css2?family=Roboto+Condensed:wght@700&family=Open+Sans:wght@400;600&family=Arimo:wght@400&display=swap" rel="stylesheet">
<style>
:root{
  --blue:#0b4f9c;
  --grey-text:#555;
  --dark:#333;
  --paper:#fff;
  --backdrop:#ecedea;
  --window:#dcdcdc;
  --badge-orange:#e9730f;
}
*{box-sizing:border-box;margin:0;padding:0}
html,body{width:1200px;height:1200px;overflow:hidden;background:#fff}
body{position:relative;font-family:"Arimo",Arial,sans-serif;color:var(--dark)}
.backdrop{position:absolute;left:0;top:240px;width:1200px;height:726px;background:var(--backdrop)}
.sheet{position:absolute;background:var(--paper);overflow:hidden}
.brand-name{font-family:"Roboto Condensed",Arial,sans-serif;font-weight:700;color:var(--blue);white-space:nowrap;position:absolute}
.bar-left,.bar-right{position:absolute;top:0;bottom:0;width:6px;background:var(--blue)}
.bar-left{left:0}.bar-right{right:0}
.marker{position:absolute;width:0;height:0;border-top:5px solid transparent;border-bottom:5px solid transparent}
.marker.right{border-left:7px solid var(--blue)}
.marker.left{border-right:7px solid var(--blue)}
.item-label{position:absolute;font-size:11px;color:#444}

/* Terms sheet */
.terms{left:34px;top:314px;width:335px;height:474px}
.terms .title{position:absolute;left:28px;top:15px;width:300px;font-family:"Open Sans",sans-serif;font-weight:600;font-size:5.2px;color:#333}
.terms .subtitle{position:absolute;left:56px;top:23px;font-family:"Open Sans",sans-serif;font-size:3.4px;color:#555}
.terms .col{position:absolute;top:36px;width:138px;height:428px;overflow:hidden;font-family:"Open Sans",sans-serif;font-size:4.3px;line-height:5.5px;color:#444;text-align:justify}
.terms .col.left{left:28px}.terms .col.right{left:175px}
.terms h4{font-weight:600;font-size:4.3px;color:#333;margin-top:5px}
.terms h4:first-child{margin-top:0}

/* Letterhead */
.letterhead{left:440px;top:314px;width:334px;height:474px}
.fold{position:absolute;left:0;width:11px;height:0;border-top:0.6px solid #999}
.sender-line{position:absolute;left:39px;top:112px;font-size:3.8px;color:#333}
.contact{position:absolute;font-size:4.4px;line-height:5.6px;color:#333}
.contact .row{display:flex;align-items:flex-start;gap:3px}
.contact .icon{width:5px;height:5px;flex:none;margin-top:0.5px}
.contact .gap{height:5px}
.footer{position:absolute;left:17px;top:443px;right:20px;display:flex;font-size:4.4px;line-height:5.2px;color:#666}
.footer .c1{width:82px}.footer .c2{width:83px}.footer .c3{width:20px;border-left:0.5px solid #aaa;padding-left:0}
.footer .c4{width:82px}
.badge{position:absolute;left:282px;top:439px;width:31px;height:22px;background:var(--blue)}
.badge::after{content:"";position:absolute;left:0;right:0;bottom:0;height:6px;background:var(--badge-orange)}

/* Logo card */
.logo-card{left:828px;top:311px;width:312px;height:164px}

/* Envelopes */
.envelope{left:808px;width:348px;height:176px}
.envelope.long{top:514px}
.envelope.window-env{top:717px}
.env-web{position:absolute;right:30px;bottom:7px;font-size:6.3px;letter-spacing:2.2px;color:#444}
.env-window{position:absolute;left:33px;top:78px;width:158px;height:69px;border-radius:4px;background:var(--window)}

/* Business cards */
.card{top:815px;width:134px;height:87px}
.card.front{left:454px}
.card.back{left:630px}
.card .person{position:absolute;left:10px;top:53px;font-size:6.2px;line-height:6.2px;color:#333;text-align:right;width:49px}
.card .contact{left:64px;top:38px;font-size:3.6px;line-height:4.4px}
.card .contact .icon{width:4px;height:4px}
.card .contact .gap{height:3px}
</style>
</head>
<body>
<div class="backdrop"></div>

<!-- Terms and conditions sheet -->
<section class="sheet terms">
  <div class="bar-left"></div>
  <div class="marker right" style="left:6px;top:12px"></div>
  <div class="title">Allgemeine Geschäftsbedingungen (AGB) · Lieferungs- und Zahlungsbedingungen der Firma KRL Fertek GmbH</div>
  <div class="subtitle">Systemlieferant für mechanische Baugruppen, Werkstraße 12, 63500 Talbach · Geschäftsführer: Herr Jonas Berger &amp; Timo Walden</div>
  <div class="col left">
    <h4>Allgemeines</h4>
    <p>Alle Angebote, Lieferungen und Leistungen erfolgen ausschließlich auf Grundlage dieser Bedingungen. Abweichende Vereinbarungen gelten nur, wenn sie schriftlich bestätigt wurden. Mit der Erteilung eines Auftrags erkennt der Auftraggeber diese Bedingungen an. Sie gelten auch für alle künftigen Geschäfte zwischen den Parteien.</p>
    <h4>Angebote und Aufträge</h4>
    <p>Unsere Angebote sind freibleibend und unverbindlich. Zeichnungen, Maße, Gewichte und Toleranzen sind nur verbindlich, wenn sie ausdrücklich vereinbart wurden. Überlassene Unterlagen bleiben unser Eigentum und dürfen Dritten nicht zugänglich gemacht werden. Für Fehler in Unterlagen des Auftraggebers übernehmen wir keine Haftung. Änderungen müssen rechtzeitig schriftlich mitgeteilt werden.</p>
    <h4>Auftragsannahme</h4>
    <p>Die Annahme eines Auftrags erfolgt durch eine schriftliche Bestätigung oder durch die Ausführung der Leistung.</p>
    <h4>Preise und Zahlungsbedingungen</h4>
    <p>Alle Preise gelten in Euro ab Werk zuzüglich der gesetzlichen Mehrwertsteuer. Verpackung, Fracht, Versicherung und Zölle werden gesondert berechnet. Rechnungen sind innerhalb von zwei Wochen ohne Abzug zahlbar. Skonto gilt nur nach schriftlicher Vereinbarung. Bei Zahlungsverzug berechnen wir Zinsen in gesetzlicher Höhe. Gerät der Auftraggeber in Verzug, dürfen wir offene Lieferungen zurückhalten. Steigen Material- oder Lohnkosten nach Vertragsschluss erheblich, behalten wir uns eine angemessene Anpassung der Preise vor. Wechsel und Schecks werden nur erfüllungshalber angenommen.</p>
    <h4>Lieferung und Lieferzeit</h4>
    <p>Die Lieferzeit beginnt erst, wenn alle technischen Fragen geklärt sind. Unvorhergesehene Störungen verlängern die Frist angemessen. Teillieferungen sind zulässig. Verzögert sich die Abnahme durch den Auftraggeber, lagern wir die Ware auf seine Kosten und Gefahr ein. Fertig gemeldete Teile gelten nach einer Woche als abgenommen.</p>
    <h4>Leistungsstörung</h4>
    <p>Können wir infolge höherer Gewalt oder Streik nicht liefern, sind wir zum Rücktritt berechtigt.</p>
  </div>
  <div class="col right">
    <h4>Gefahrenübergang</h4>
    <p>Die Gefahr geht auf den Auftraggeber über, sobald die Ware das Werk verlassen hat oder dem Spediteur übergeben wurde. Dies gilt auch bei frachtfreier Lieferung.</p>
    <h4>Mängelrüge</h4>
    <p>Mängel sind unverzüglich, spätestens sieben Tage nach Erhalt der Ware, schriftlich anzuzeigen. Versteckte Mängel sind sofort nach ihrer Entdeckung zu melden. Bei berechtigter Rüge bessern wir nach oder liefern Ersatz. Weitergehende Ansprüche, insbesondere auf Ersatz von Folgeschäden, sind ausgeschlossen, soweit gesetzlich zulässig. Für beigestellte Teile des Auftraggebers übernehmen wir keine Haftung.</p>
    <h4>Eigentumsvorbehalt</h4>
    <p>Die gelieferte Ware bleibt bis zur vollständigen Bezahlung aller Forderungen unser Eigentum. Der Auftraggeber darf sie im gewöhnlichen Geschäftsverkehr verarbeiten oder veräußern. Die daraus entstehenden Forderungen tritt er bereits jetzt an uns ab. Verpfändungen und Sicherungsübereignungen sind nicht gestattet. Zugriffe Dritter sind uns sofort mitzuteilen. Übersteigt der Wert der Sicherheiten unsere Forderungen um mehr als zehn Prozent, geben wir sie auf Verlangen frei.</p>
    <h4>Schlussbestimmungen</h4>
    <p>Beide Parteien behandeln alle Unterlagen vertraulich. Daten werden nur im Rahmen der Geschäftsbeziehung gespeichert und verarbeitet. Sollte eine Bestimmung unwirksam sein, bleiben die übrigen Bestimmungen gültig.</p>
    <p style="margin-top:3px">Es gilt ausschließlich deutsches Recht.</p>
    <h4>Erfüllungsort und Gerichtsstand</h4>
    <p>Erfüllungsort für alle Leistungen ist unser Firmensitz. Gerichtsstand ist das zuständige Amtsgericht.</p>
  </div>
</section>

<!-- Letterhead -->
<section class="sheet letterhead">
  <div class="bar-right"></div>
  <div class="marker left" style="right:6px;top:81px"></div>
  <div class="fold" style="top:170px"></div>
  <div class="fold" style="top:240px"></div>
  <div class="fold" style="top:338px"></div>
  <div class="brand-name" style="left:14px;top:24px;font-size:17px">KRL Fertek GmbH</div>
  <div class="sender-line">KRL Fertek GmbH | Werkstraße 12 · 63500 Talbach</div>
  <div class="contact" style="left:199px;top:83px">
    <div class="row">
      <svg class="icon" viewBox="0 0 10 10"><path d="M5 0.5a3.3 3.3 0 0 0-3.3 3.3C1.7 6.3 5 9.5 5 9.5s3.3-3.2 3.3-5.7A3.3 3.3 0 0 0 5 .5z" fill="var(--blue)"/><circle cx="5" cy="3.8" r="1.2" fill="#fff"/></svg>
      <div>KRL Fertek GmbH<br>Werkstraße 12<br>63500 Talbach</div>
    </div>
    <div class="gap"></div>
    <div class="row">
      <svg class="icon" viewBox="0 0 10 10"><path d="M1 3.5C1 2 3 1.5 5 1.5S9 2 9 3.5H6.8V2.8H3.2v.7zM2 5h6l1 4H1z" fill="var(--blue)"/></svg>
      <div>+49 (0) 6000/12345 0</div>
    </div>
    <div class="row">
      <svg class="icon" viewBox="0 0 10 10"><rect x="2.5" y="1" width="5" height="3" fill="var(--blue)"/><rect x="1" y="4" width="8" height="4" rx="1" fill="var(--blue)"/><rect x="3" y="7" width="4" height="2.5" fill="var(--blue)"/></svg>
      <div>+49 (0) 6000/12345 20</div>
    </div>
    <div class="row">
      <svg class="icon" viewBox="0 0 10 10"><rect x="1" y="2.5" width="8" height="5.5" fill="var(--blue)"/><path d="M1 2.5l4 3 4-3" stroke="#fff" stroke-width="0.8" fill="none"/></svg>
      <div>info@krl-fertek.de</div>
    </div>
    <div class="row">
      <svg class="icon" viewBox="0 0 10 10"><circle cx="5" cy="5" r="4" fill="none" stroke="var(--blue)" stroke-width="1"/><path d="M1 5h8M5 1c-2 2.5-2 5.5 0 8M5 1c2 2.5 2 5.5 0 8" stroke="var(--blue)" stroke-width="0.7" fill="none"/></svg>
      <div>www.krl-fertek.de</div>
    </div>
  </div>
  <div class="footer">
    <div class="c1">Handelsregister Eintrag<br>Geschäftsführer<br>gemäß § 27 a Umsatzsteuergesetz<br>USt-Id-Nr.</div>
    <div class="c2">AG Talbach HRB 12 34<br>Jonas Berger &amp; Timo Walden<br>012 345 67890<br>DE 123456789</div>
    <div class="c3">Bank<br>IBAN<br>BIC</div>
    <div class="c4">Rheintal Sparkasse<br>DE00 1234 5678 0000 1111 22<br>RHTADE00XXX</div>
  </div>
  <div class="badge" role="img" aria-label="Zertifizierungssiegel"></div>
</section>

<!-- Logo card -->
<section class="sheet logo-card">
  <div class="brand-name" style="left:0;right:0;top:58px;text-align:center;font-size:38px">KRL Fertek GmbH</div>
</section>

<!-- Envelope DL -->
<span class="item-label" style="left:793px;top:514px">1</span>
<section class="sheet envelope long">
  <div class="bar-right"></div>
  <div class="brand-name" style="left:12px;top:25px;font-size:13px">KRL Fertek GmbH</div>
  <div class="marker left" style="right:6px;bottom:8px"></div>
  <div class="env-web">www.krl-fertek.de</div>
</section>

<!-- Envelope with window -->
<span class="item-label" style="left:793px;top:717px">3</span>
<section class="sheet envelope window-env">
  <div class="bar-right"></div>
  <div class="brand-name" style="left:12px;top:25px;font-size:13px">KRL Fertek GmbH</div>
  <div class="env-window"></div>
  <div class="marker left" style="right:6px;bottom:8px"></div>
  <div class="env-web">www.krl-fertek.de</div>
</section>

<!-- Business card front -->
<span class="item-label" style="left:428px;top:818px">1</span>
<section class="sheet card front">
  <div class="brand-name" style="left:0;right:0;top:34px;text-align:center;font-size:15px">KRL Fertek GmbH</div>
</section>

<!-- Business card back -->
<span class="item-label" style="left:612px;top:818px">A</span>
<section class="sheet card back">
  <div class="bar-left"></div>
  <div class="marker right" style="left:6px;top:56px"></div>
  <div class="brand-name" style="left:10px;top:6px;font-size:12px">KRL Fertek GmbH</div>
  <div class="person">Jonas Rolvex<br>Leiter Einkauf</div>
  <div class="contact">
    <div class="row">
      <svg class="icon" viewBox="0 0 10 10"><path d="M5 0.5a3.3 3.3 0 0 0-3.3 3.3C1.7 6.3 5 9.5 5 9.5s3.3-3.2 3.3-5.7A3.3 3.3 0 0 0 5 .5z" fill="var(--blue)"/><circle cx="5" cy="3.8" r="1.2" fill="#fff"/></svg>
      <div>KRL Fertek GmbH<br>Werkstraße 12<br>63500 Talbach</div>
    </div>
    <div class="gap"></div>
    <div class="row">
      <svg class="icon" viewBox="0 0 10 10"><path d="M1 3.5C1 2 3 1.5 5 1.5S9 2 9 3.5H6.8V2.8H3.2v.7zM2 5h6l1 4H1z" fill="var(--blue)"/></svg>
      <div>+49 (0) 6000 / 12345 21</div>
    </div>
    <div class="row">
      <svg class="icon" viewBox="0 0 10 10"><rect x="2.5" y="1" width="5" height="3" fill="var(--blue)"/><rect x="1" y="4" width="8" height="4" rx="1" fill="var(--blue)"/><rect x="3" y="7" width="4" height="2.5" fill="var(--blue)"/></svg>
      <div>+49 (0) 6000 / 12345 39</div>
    </div>
    <div class="row">
      <svg class="icon" viewBox="0 0 10 10"><rect x="3" y="0.5" width="4" height="9" rx="0.8" fill="none" stroke="var(--blue)" stroke-width="1"/></svg>
      <div>+49 (0) 170 / 1234567</div>
    </div>
    <div class="row">
      <svg class="icon" viewBox="0 0 10 10"><rect x="1" y="2.5" width="8" height="5.5" fill="var(--blue)"/><path d="M1 2.5l4 3 4-3" stroke="#fff" stroke-width="0.8" fill="none"/></svg>
      <div>rolvex@krl-fertek.de</div>
    </div>
    <div class="row">
      <svg class="icon" viewBox="0 0 10 10"><circle cx="5" cy="5" r="4" fill="none" stroke="var(--blue)" stroke-width="1"/><path d="M1 5h8M5 1c-2 2.5-2 5.5 0 8M5 1c2 2.5 2 5.5 0 8" stroke="var(--blue)" stroke-width="0.7" fill="none"/></svg>
      <div>www.krl-fertek.de</div>
    </div>
  </div>
</section>
</body>
</html>
```